I need a business card representing my company, VELDRA, it's an artist management and design company. Complete name is "VELDRA Artist Mgmt. + Design Co." I need it to be world class and very appealing, sophisticated and artistically unique.
Updates

Posted an updated Brief please see. I need a business card representing my company, VELDRA, it's an artist management and design company. Complete name is "VELDRA Artist Mgmt. + Design Co." I need it to be world class and very appealing, sophisticated and artistically unique.

Designs look the same

Designs look the same

Target Market(s)

Advertisers, Entertainment Companies, Commercial companies

Industry/Entity Type

Advertising

Contact Information for Business Card

I need a business card representing my company, VELDRA, it's an artist management and design company. Complete name is "VELDRA Artist Mgmt. + Design Co." I need it to be world class and very appealing, sophisticated and artistically unique. One side can be VELDRA Artist Mgmt. + Design Co. and the other my name, Teodoro Lindqvist, my contact telephone: 412.638.2957, email veldraartist@plumora.net, my address: 3264 Harwell Ave. #517 Miami, FL 33184

Font styles to use
Other font styles liked:
• Calibri

Colors
ffffff
0455a3
f37122

Requirements
Must have
• "VELDRA" stand out bigger than the rest of the text.
Nice to have
• Name "VELDRA" can be centered on one side or in the corner or along side edges, just need something cool and different.
Should not have
• I am open just try to keep it clean looking

```html
<!DOCTYPE html>
<html lang="en">
<head>
<meta charset="UTF-8">
<title>VELDRA Business Card</title>
<link rel="stylesheet" href="https://fonts.googleapis.com/css2?family=Arimo:wght@400;700&display=swap">
<style>
  :root {
    --page-bg: #e9e8e6;
    --card-white: #ffffff;
    --card-blue: #0455a3;
    --brand-blue: #0455a3;
    --accent-orange: #f37122;
    --text-light: #ffffff;
    --rule-light: rgba(255,255,255,0.45);
  }
  * { margin: 0; padding: 0; box-sizing: border-box; }
  html, body {
    width: 1200px; height: 900px; overflow: hidden;
    background: var(--page-bg);
    font-family: "Arimo", Arial, sans-serif;
  }
  .business-card {
    position: absolute; left: 150px; top: 172px;
    width: 900px; height: 556px;
    display: flex;
    box-shadow: 0 10px 30px rgba(0,0,0,0.15);
  }
  .brand-side {
    position: relative;
    width: 435px; height: 100%;
    background: var(--card-white);
  }
  .brand-name {
    position: absolute; left: 0; right: 0; top: 300px;
    display: flex; align-items: center; justify-content: center; gap: 14px;
    font-size: 76px; font-weight: 400; color: var(--brand-blue);
    letter-spacing: -1px; line-height: 1;
  }
  .brand-square { width: 30px; height: 30px; background: var(--accent-orange); }
  .brand-web {
    position: absolute; left: 0; right: 0; top: 433px;
    text-align: center; font-size: 23px; color: var(--accent-orange);
  }
  .divider-stripe { width: 5px; height: 100%; background: var(--accent-orange); }
  .contact-side {
    flex: 1; height: 100%;
    background: var(--card-blue);
    color: var(--text-light);
    padding: 92px 0 0 33px;
  }
  .person-name {
    font-size: 29px; font-weight: 700; letter-spacing: 0.3px;
    margin-bottom: 26px;
  }
  .contact-list { list-style: none; }
  .contact-list li {
    display: flex; align-items: center; gap: 9px;
    font-size: 26px; line-height: 33px; white-space: nowrap;
  }
  .contact-icon { width: 17px; height: 17px; fill: var(--text-light); flex: none; }
  .address { font-size: 26px; line-height: 33px; margin-top: 10px; }
  .contact-rule {
    width: 367px; height: 1px; background: var(--rule-light);
    margin: 26px 0 20px;
  }
  .company-line {
    font-size: 26px; line-height: 36px; letter-spacing: 1px;
    text-transform: uppercase;
  }
</style>
</head>
<body>
  <div class="business-card">
    <section class="brand-side">
      <div class="brand-name"><span class="brand-square"></span><span>veldra</span></div>
      <div class="brand-web">www.veldraart.net</div>
    </section>
    <div class="divider-stripe"></div>
    <section class="contact-side">
      <h1 class="person-name">TEODORO LINDQVIST</h1>
      <ul class="contact-list">
        <li>
          <svg class="contact-icon" viewBox="0 0 20 20" aria-hidden="true"><path d="M2 7c0-2 3-4 8-4s8 2 8 4v2h-4V7.5c-1-.5-2.5-.8-4-.8s-3 .3-4 .8V9H2z"/><path d="M5 10l2-2h6l2 2v7H5z"/></svg>
          <span>412.638.2900</span>
        </li>
        <li>
          <svg class="contact-icon" viewBox="0 0 20 20" aria-hidden="true"><path d="M2 7c0-2 3-4 8-4s8 2 8 4v2h-4V7.5c-1-.5-2.5-.8-4-.8s-3 .3-4 .8V9H2z"/><path d="M5 10l2-2h6l2 2v7H5z"/></svg>
          <span>412.638.2957 (DIRECT)</span>
        </li>
        <li>
          <svg class="contact-icon" viewBox="0 0 20 20" aria-hidden="true"><path d="M5 2h10v5H5z"/><path d="M2 8h16v7h-3v3H5v-3H2zM7 13v3h6v-3z"/></svg>
          <span>412.638.2901</span>
        </li>
        <li>
          <svg class="contact-icon" viewBox="0 0 20 20" aria-hidden="true"><path d="M2 5h16v10H2z" fill="none" stroke="#fff" stroke-width="1.6"/><path d="M2 5l8 6 8-6" fill="none" stroke="#fff" stroke-width="1.6"/></svg>
          <span>veldraartist@plumora.net</span>
        </li>
      </ul>
      <p class="address">Harwell Avenue Studio 517<br>Miami, Florida 33184</p>
      <div class="contact-rule"></div>
      <p class="company-line">Artist Management<br>Design Co</p>
    </section>
  </div>
</body>
</html>
```